Search Fund needs a PowerPoint template design

We need a eye-catching and compelling PowerPoint design for a new company based in Chicago called Tarn Ridge Partners. We are search fund with a primary mission to acquire a founder/family/entrepreneur owned businesses (This is similar to a Private Equity firm). Our goal is to offer investors a unique avenue to invest in an attractive business acquisition while providing business owners with an alternative path to exit. We would like the design to reflect crisp and professional nature that many financial firms present. The template should build on the design of the logo including expanding a logical color palette. The presentation will be used to describe facts regarding the firm, financial data and key messaging that we want our investors and potential partners to takeaway.

Target Market(s)

Financial Investors

Industry/Entity Type

Finance

Font styles to use
Serif
Sans Serif

Colors

Designer to choose colors to be used in the design.

Requirements
Must have
• Should include cover page and slide examples. Attractive data displays (graphs, charts, infographics etc.); Compelling cover; fly pages to put in between sections; table of contents page. Needs to have white space to add text.
Should not have
• Do not redesign the logo or change the logo colors. Additional colors should be added to the PowerPoint template

```html
<!DOCTYPE html>
<html lang="en">
<head>
<meta charset="utf-8">
<title>Tarn Ridge Partners — Presentation Template</title>
<link href="https://fonts.googleapis.com/css2?family=Open+Sans:wght@400;600;700;800&display=swap" rel="stylesheet">
<style>
:root{
  --bg:#d4d5d8;
  --blue:#1f6fc0;
  --blue-dark:#175595;
  --blue-deep:#123f70;
  --ink:#2e3440;
  --muted:#8a8f97;
  --line:#c9ccd1;
  --panel:#eceef1;
  --white:#ffffff;
}
*{box-sizing:border-box;margin:0;padding:0}
html,body{width:934px;height:1200px;overflow:hidden;background:var(--bg)}
body{font-family:"Open Sans",Arial,sans-serif;color:var(--ink)}
.canvas{position:relative;width:934px;height:1200px;background:var(--bg)}
.slide{position:absolute;width:184px;height:104px;background:var(--white);overflow:hidden;box-shadow:0 1px 2px rgba(0,0,0,.18)}
.slide-title{position:absolute;left:6px;top:5px;font-size:3.6px;font-weight:700;letter-spacing:.1px;color:var(--ink);padding-left:2px;border-left:.8px solid var(--blue);line-height:1}
.slide-title.blue{color:var(--blue-dark)}
.footer{position:absolute;left:6px;bottom:4px;right:6px;border-top:.3px solid var(--line);padding-top:1px;font-size:2.4px;font-weight:800;color:var(--blue);line-height:1}
.p{position:absolute;font-size:2.1px;line-height:1.35;color:var(--muted)}
.p.w{color:#e6eefa}
.h{position:absolute;font-size:2.4px;font-weight:700;color:var(--blue-dark);line-height:1.2}
.h.w{color:#fff}
.abs{position:absolute}
.photo{position:absolute;background:linear-gradient(135deg,#7fa8d4,#2c5f99)}
.photo.warm{background:linear-gradient(135deg,#c9b7a3,#6d7d8e)}
.photo.grey{background:linear-gradient(135deg,#c7ccd3,#7c8795)}
.photo.dark{background:linear-gradient(135deg,#3a6aa6,#0f2f57)}
.band{position:absolute;background:var(--blue)}
.ico{position:absolute;border-radius:50%;background:var(--blue)}
.ico::after{content:"";position:absolute;left:30%;top:30%;width:40%;height:40%;background:#fff;border-radius:1px}
.ico.w{background:#fff}
.ico.w::after{background:var(--blue)}
.box{position:absolute;background:var(--blue);color:#fff;font-size:2.2px;font-weight:700;display:flex;align-items:center;justify-content:center;text-align:center;line-height:1.1}
.box.grey{background:#7d838c}
svg{position:absolute;overflow:visible}
</style>
</head>
<body>
<main class="canvas">

<!-- Row 1 -->
<section class="slide cover" style="left:60px;top:48px">
  <div class="photo" style="left:0;top:0;width:184px;height:78px;background:linear-gradient(120deg,#2f78c6,#1b5ea8 60%,#5e91c7)" role="img" aria-label="Business team reviewing documents, blue toned photo"></div>
  <div class="abs" style="left:16px;top:20px;width:92px;font-size:6.6px;font-weight:700;line-height:1.12;color:#fff">Lorem ipsum dolor sit amet, consectetur adipiscing elit, sed do eiusmod tempor</div>
  <div class="abs" style="left:12px;top:87px;font-size:5px;font-weight:800;color:var(--blue-dark);line-height:1">TARN RIDGE PARTNERS</div>
  <div class="abs" style="right:10px;top:89px;font-size:2.6px;font-weight:700;color:var(--blue-dark)">www.TarnRidge.example</div>
</section>

<section class="slide" style="left:266px;top:48px">
  <div class="slide-title">ABOUT US</div>
  <div class="band" style="left:10px;top:23px;width:70px;height:70px"></div>
  <div class="p w" style="left:14px;top:30px;width:48px">Lorem ipsum dolor sit amet, consectetur adipiscing elit, sed do eiusmod tempor incididunt ut labore et dolore magna aliqua. Ut enim ad minim veniam, quis nostrud exercitation ullamco laboris nisi ut aliquip ex ea commodo.</div>
  <div class="photo dark" style="left:80px;top:23px;width:96px;height:70px" role="img" aria-label="Hands using a tablet with data graphics"></div>
  <div class="footer">TARN RIDGE</div>
</section>

<section class="slide" style="left:472px;top:48px">
  <div class="slide-title">OUR TEAM</div>
  <div class="photo grey" style="left:24px;top:18px;width:20px;height:20px;border-radius:50%" role="img" aria-label="Team member portrait"></div>
  <div class="photo grey" style="left:66px;top:18px;width:20px;height:20px;border-radius:50%" role="img" aria-label="Team member portrait"></div>
  <div class="photo grey" style="left:108px;top:18px;width:20px;height:20px;border-radius:50%" role="img" aria-label="Team member portrait"></div>
  <div class="photo grey" style="left:150px;top:18px;width:20px;height:20px;border-radius:50%" role="img" aria-label="Team member portrait"></div>
  <div class="h" style="left:22px;top:41px;width:24px;text-align:center">CLARA WYNN</div>
  <div class="h" style="left:64px;top:41px;width:24px;text-align:center">OWEN HALE</div>
  <div class="h" style="left:106px;top:41px;width:24px;text-align:center">MILES FORD</div>
  <div class="h" style="left:148px;top:41px;width:24px;text-align:center">EVAN COLE</div>
  <div class="p" style="left:22px;top:50px;width:150px;text-align:center">Lorem ipsum dolor sit amet, consectetur adipiscing elit, sed do eiusmod tempor incididunt ut labore et dolore magna aliqua. Ut enim ad minim veniam, quis nostrud exercitation ullamco laboris nisi ut aliquip ex ea commodo consequat.</div>
  <div class="footer">TARN RIDGE</div>
</section>

<section class="slide" style="left:678px;top:48px">
  <div class="slide-title">EDIT TITLE HERE</div>
  <div class="photo" style="left:10px;top:17px;width:52px;height:38px" role="img" aria-label="Desk with charts"></div>
  <div class="photo grey" style="left:66px;top:17px;width:52px;height:38px" role="img" aria-label="Laptop with data"></div>
  <div class="photo dark" style="left:122px;top:17px;width:52px;height:38px" role="img" aria-label="City skyline"></div>
  <div class="h" style="left:10px;top:58px;width:52px;text-align:center">LOREM IPSUM</div>
  <div class="h" style="left:66px;top:58px;width:52px;text-align:center">LOREM IPSUM</div>
  <div class="h" style="left:122px;top:58px;width:52px;text-align:center">LOREM IPSUM</div>
  <div class="p" style="left:12px;top:62px;width:48px;text-align:center">Lorem ipsum dolor sit amet, consectetur adipiscing elit sed do eiusmod.</div>
  <div class="p" style="left:68px;top:62px;width:48px;text-align:center">Lorem ipsum dolor sit amet, consectetur adipiscing elit sed do eiusmod.</div>
  <div class="p" style="left:124px;top:62px;width:48px;text-align:center">Lorem ipsum dolor sit amet, consectetur adipiscing elit sed do eiusmod.</div>
  <div class="footer">TARN RIDGE</div>
</section>

<!-- Row 2 -->
<section class="slide" style="left:60px;top:171px">
  <div class="slide-title">OUR SERVICES</div>
  <div class="abs" style="left:0;top:18px;width:184px;height:72px;background:var(--panel)"></div>
  <div class="ico" style="left:27px;top:26px;width:6px;height:6px"></div>
  <div class="ico" style="left:57px;top:26px;width:6px;height:6px"></div>
  <div class="ico" style="left:87px;top:26px;width:6px;height:6px"></div>
  <div class="ico" style="left:117px;top:26px;width:6px;height:6px"></div>
  <div class="ico" style="left:147px;top:26px;width:6px;height:6px"></div>
  <div class="ico" style="left:27px;top:56px;width:6px;height:6px"></div>
  <div class="ico" style="left:57px;top:56px;width:6px;height:6px"></div>
  <div class="ico" style="left:87px;top:56px;width:6px;height:6px"></div>
  <div class="ico" style="left:117px;top:56px;width:6px;height:6px"></div>
  <div class="ico" style="left:147px;top:56px;width:6px;height:6px"></div>
  <div class="h" style="left:18px;top:35px;width:24px;text-align:center">LOREM IPSUM</div>
  <div class="h" style="left:48px;top:35px;width:24px;text-align:center">LOREM IPSUM</div>
  <div class="h" style="left:78px;top:35px;width:24px;text-align:center">LOREM IPSUM</div>
  <div class="h" style="left:108px;top:35px;width:24px;text-align:center">LOREM IPSUM</div>
  <div class="h" style="left:138px;top:35px;width:24px;text-align:center">LOREM IPSUM</div>
  <div class="h" style="left:18px;top:65px;width:24px;text-align:center">LOREM IPSUM</div>
  <div class="h" style="left:48px;top:65px;width:24px;text-align:center">LOREM IPSUM</div>
  <div class="h" style="left:78px;top:65px;width:24px;text-align:center">LOREM IPSUM</div>
  <div class="h" style="left:108px;top:65px;width:24px;text-align:center">LOREM IPSUM</div>
  <div class="h" style="left:138px;top:65px;width:24px;text-align:center">LOREM IPSUM</div>
  <div class="footer">TARN RIDGE</div>
</section>

<section class="slide" style="left:266px;top:171px">
  <div class="slide-title">EDIT TITLE HERE</div>
  <svg width="184" height="104" viewBox="0 0 184 104"><g stroke="#8a8f97" stroke-width=".4" fill="none">
    <path d="M42 32 H130 M60 32 V80 M60 59 H70 M60 80 H70 M98 35 V80 M94 59 H100 M94 80 H100"/></g></svg>
  <div class="box" style="left:14px;top:28px;width:28px;height:8px">TRAINING</div>
  <div class="box" style="left:84px;top:28px;width:28px;height:7px">LEVEL</div>
  <div class="box grey" style="left:130px;top:28px;width:26px;height:7px">LEVEL</div>
  <div class="box grey" style="left:70px;top:56px;width:24px;height:7px">LEVEL</div>
  <div class="box" style="left:100px;top:56px;width:24px;height:7px">LEVEL</div>
  <div class="box grey" style="left:130px;top:56px;width:24px;height:7px">LEVEL</div>
  <div class="box grey" style="left:70px;top:77px;width:24px;height:7px">LEVEL</div>
  <div class="box" style="left:100px;top:77px;width:24px;height:7px">LEVEL</div>
  <div class="box grey" style="left:130px;top:77px;width:24px;height:7px">LEVEL</div>
  <div class="footer">TARN RIDGE</div>
</section>

<section class="slide" style="left:472px;top:171px">
  <div class="slide-title">EDIT TITLE HERE</div>
  <div class="box grey" style="left:44px;top:19px;width:22px;height:4px">LOREM</div>
  <div class="box grey" style="left:70px;top:19px;width:22px;height:4px">LOREM</div>
  <div class="box grey" style="left:96px;top:19px;width:22px;height:4px">LOREM</div>
  <div class="box grey" style="left:122px;top:19px;width:22px;height:4px">LOREM</div>
  <div class="box grey" style="left:148px;top:19px;width:22px;height:4px">LOREM</div>
  <div class="box grey" style="left:14px;top:28px;width:22px;height:10px">LOREM</div>
  <div class="box grey" style="left:14px;top:41px;width:22px;height:10px">LOREM</div>
  <div class="box grey" style="left:14px;top:54px;width:22px;height:10px">LOREM</div>
  <div class="box grey" style="left:14px;top:67px;width:22px;height:10px">LOREM</div>
  <div class="box grey" style="left:14px;top:80px;width:22px;height:10px">LOREM</div>
  <svg width="184" height="104" viewBox="0 0 184 104"><g fill="#1f6fc0">
    <rect x="44" y="28" width="22" height="10"/><rect x="70" y="28" width="22" height="10"/><rect x="96" y="28" width="22" height="10"/><rect x="122" y="28" width="22" height="10"/><rect x="148" y="28" width="22" height="10"/>
    <rect x="44" y="41" width="22" height="10"/><rect x="70" y="41" width="22" height="10"/><rect x="96" y="41" width="22" height="10"/><rect x="122" y="41" width="22" height="10"/><rect x="148" y="41" width="22" height="10"/>
    <rect x="44" y="54" width="22" height="10"/><rect x="70" y="54" width="22" height="10"/><rect x="96" y="54" width="22" height="10"/><rect x="122" y="54" width="22" height="10"/><rect x="148" y="54" width="22" height="10"/>
    <rect x="44" y="67" width="22" height="10"/><rect x="70" y="67" width="22" height="10"/><rect x="96" y="67" width="22" height="10"/><rect x="122" y="67" width="22" height="10"/><rect x="148" y="67" width="22" height="10"/>
    <rect x="44" y="80" width="22" height="10"/><rect x="70" y="80" width="22" height="10"/><rect x="96" y="80" width="22" height="10"/><rect x="122" y="80" width="22" height="10"/><rect x="148" y="80" width="22" height="10"/>
  </g></svg>
  <div class="footer">TARN RIDGE</div>
</section>

<section class="slide" style="left:678px;top:171px">
  <div class="slide-title">EDIT TITLE HERE</div>
  <div class="p" style="left:12px;top:20px;width:108px">Lorem ipsum dolor sit amet, consectetur adipiscing elit, sed do eiusmod tempor incididunt ut labore et dolore magna aliqua. Ut enim ad minim veniam, quis nostrud exercitation ullamco laboris nisi ut aliquip ex ea commodo consequat. Duis aute irure dolor in reprehenderit in voluptate velit esse cillum dolore eu fugiat nulla pariatur.</div>
  <div class="ico" style="left:26px;top:60px;width:6px;height:6px;border-radius:1px"></div>
  <div class="ico" style="left:60px;top:60px;width:6px;height:6px;border-radius:1px"></div>
  <div class="ico" style="left:94px;top:60px;width:6px;height:6px;border-radius:1px"></div>
  <div class="p" style="left:14px;top:69px;width:30px;text-align:center">Lorem ipsum dolor</div>
  <div class="p" style="left:48px;top:69px;width:30px;text-align:center">Lorem ipsum dolor</div>
  <div class="p" style="left:82px;top:69px;width:30px;text-align:center">Lorem ipsum dolor</div>
  <div class="photo warm" style="left:126px;top:0;width:58px;height:104px" role="img" aria-label="Colleagues meeting in an office"></div>
  <div class="footer" style="right:64px">TARN RIDGE</div>
</section>

<!-- Row 3 -->
<section class="slide" style="left:60px;top:294px">
  <div class="slide-title">EDIT TITLE HERE</div>
  <svg width="184" height="104" viewBox="0 0 184 104">
    <path d="M14 20 V76 H84" stroke="#c9ccd1" stroke-width=".4" fill="none"/>
    <g fill="#1f6fc0"><rect x="20" y="66" width="5" height="10"/><rect x="42" y="58" width="5" height="18" fill="#175595"/><rect x="64" y="46" width="5" height="30"/></g>
    <g fill="#8a8f97"><rect x="31" y="62" width="5" height="14"/><rect x="53" y="52" width="5" height="24"/><rect x="75" y="32" width="5" height="44" fill="#1f6fc0"/></g>
    <polyline points="22,66 33,60 44,56 55,50 66,44 77,30" stroke="#1f6fc0" stroke-width=".6" fill="none"/>
    <g fill="#1f6fc0"><circle cx="22" cy="66" r=".9"/><circle cx="33" cy="60" r=".9"/><circle cx="44" cy="56" r=".9"/><circle cx="55" cy="50" r=".9"/><circle cx="66" cy="44" r=".9"/><circle cx="77" cy="30" r=".9"/></g>
    <g fill="#1f6fc0"><circle cx="18" cy="84" r="1.6"/><circle cx="34" cy="84" r="1.6"/><circle cx="50" cy="84" r="1.6" fill="#8a8f97"/><circle cx="66" cy="84" r="1.6" fill="#175595"/><circle cx="82" cy="84" r="1.6"/></g>
  </svg>
  <div class="p" style="left:100px;top:14px;width:74px">Lorem ipsum dolor sit amet, consectetur adipiscing elit, sed do eiusmod tempor incididunt ut labore et dolore magna aliqua. Ut enim ad minim veniam, quis nostrud exercitation ullamco laboris nisi ut aliquip ex ea commodo consequat. Duis aute irure dolor in reprehenderit in voluptate velit esse cillum dolore eu fugiat nulla pariatur. Excepteur sint occaecat cupidatat non proident, sunt in culpa qui officia deserunt mollit anim id est laborum sed ut perspiciatis.</div>
  <div class="footer">TARN RIDGE</div>
</section>

<section class="slide" style="left:266px;top:294px">
  <div class="photo dark" style="left:0;top:0;width:184px;height:104px;background:linear-gradient(90deg,#2b64a6,#6f95c2 55%,#304e78)" role="img" aria-label="Financial data screens with city overlay"></div>
  <div class="abs" style="left:0;top:0;width:84px;height:104px;background:rgba(31,111,192,.8)"></div>
  <div class="abs" style="left:12px;top:33px;width:60px;text-align:center;font-size:6px;font-weight:700;color:#fff">Section Title</div>
  <div class="p w" style="left:14px;top:44px;width:56px;text-align:center;font-size:2.5px">Lorem ipsum dolor sit amet, consectetur adipiscing elit. Curabitur adipiscing ultrices mauris, vel magna sed finibus felis ullamcorper imperdiet ultrices dictum.</div>
</section>

<section class="slide" style="left:472px;top:294px">
  <div class="slide-title">EDIT TITLE HERE</div>
  <svg width="184" height="104" viewBox="0 0 184 104"><line x1="92" y1="22" x2="92" y2="90" stroke="#c9ccd1" stroke-width=".4"/></svg>
  <div class="ico" style="left:76px;top:24px;width:7px;height:7px"></div>
  <div class="ico" style="left:76px;top:42px;width:7px;height:7px"></div>
  <div class="ico" style="left:76px;top:60px;width:7px;height:7px"></div>
  <div class="ico" style="left:76px;top:76px;width:7px;height:7px"></div>
  <div class="ico" style="left:100px;top:24px;width:7px;height:7px;background:#7d838c"></div>
  <div class="ico" style="left:100px;top:42px;width:7px;height:7px;background:#7d838c"></div>
  <div class="ico" style="left:100px;top:60px;width:7px;height:7px;background:#7d838c"></div>
  <div class="ico" style="left:100px;top:76px;width:7px;height:7px;background:#7d838c"></div>
  <div class="p" style="left:20px;top:24px;width:52px;text-align:right"><b style="color:#175595">Lorem ipsum dolor</b><br>Sit amet, consectetur adipiscing elit sed do.</div>
  <div class="p" style="left:20px;top:42px;width:52px;text-align:right"><b style="color:#175595">Lorem ipsum dolor</b><br>Sit amet, consectetur adipiscing elit sed do.</div>
  <div class="p" style="left:20px;top:60px;width:52px;text-align:right"><b style="color:#175595">Lorem ipsum dolor</b><br>Sit amet, consectetur adipiscing elit sed do.</div>
  <div class="p" style="left:20px;top:76px;width:52px;text-align:right"><b style="color:#175595">Lorem ipsum dolor</b><br>Sit amet, consectetur adipiscing elit sed do.</div>
  <div class="p" style="left:111px;top:24px;width:52px"><b style="color:#175595">Lorem ipsum dolor</b><br>Sit amet, consectetur adipiscing elit sed do.</div>
  <div class="p" style="left:111px;top:42px;width:52px"><b style="color:#175595">Lorem ipsum dolor</b><br>Sit amet, consectetur adipiscing elit sed do.</div>
  <div class="p" style="left:111px;top:60px;width:52px"><b style="color:#175595">Lorem ipsum dolor</b><br>Sit amet, consectetur adipiscing elit sed do.</div>
  <div class="p" style="left:111px;top:76px;width:52px"><b style="color:#175595">Lorem ipsum dolor</b><br>Sit amet, consectetur adipiscing elit sed do.</div>
  <div class="footer">TARN RIDGE</div>
</section>

<section class="slide" style="left:678px;top:294px">
  <div class="slide-title">EDIT TITLE HERE</div>
  <div class="photo" style="left:0;top:16px;width:184px;height:68px;background:linear-gradient(90deg,#1f6fc0 50%,#7fa8d4)" role="img" aria-label="Office workspace photo in blue tones"></div>
  <div class="p w" style="left:10px;top:23px;width:36px;font-size:2.4px">Lorem ipsum dolor sit amet consectetur adipiscing elit. Cras bibendum mattis leo, ac efficitur ipsum lobortis nec. Phasellus vitae pulvinar lorem.</div>
  <div class="abs" style="left:54px;top:36px;width:112px;height:34px;background:#fff"></div>
  <div class="ico" style="left:76px;top:44px;width:6px;height:6px;border-radius:1px"></div>
  <div class="ico" style="left:106px;top:44px;width:6px;height:6px;border-radius:1px"></div>
  <div class="ico" style="left:136px;top:44px;width:6px;height:6px;border-radius:1px"></div>
  <div class="h" style="left:69px;top:55px;width:20px;text-align:center;color:var(--ink)">LOREM</div>
  <div class="h" style="left:99px;top:55px;width:20px;text-align:center;color:var(--ink)">LOREM</div>
  <div class="h" style="left:129px;top:55px;width:20px;text-align:center;color:var(--ink)">LOREM</div>
  <div class="footer">TARN RIDGE</div>
</section>

<!-- Row 4 -->
<section class="slide" style="left:60px;top:418px">
  <div class="slide-title">EDIT TITLE HERE</div>
  <div class="abs" style="left:26px;top:20px;width:36px;height:30px;border:.4px solid var(--blue)"></div>
  <div class="abs" style="left:72px;top:20px;width:36px;height:30px;border:.4px solid var(--blue)"></div>
  <div class="abs" style="left:118px;top:20px;width:36px;height:30px;border:.4px solid var(--blue)"></div>
  <div class="abs" style="left:26px;top:58px;width:36px;height:30px;border:.4px solid var(--blue)"></div>
  <div class="abs" style="left:72px;top:58px;width:36px;height:30px;border:.4px solid var(--blue)"></div>
  <div class="abs" style="left:118px;top:58px;width:36px;height:30px;border:.4px solid var(--blue)"></div>
  <svg width="184" height="104" viewBox="0 0 184 104"><g fill="#1f6fc0">
    <path d="M40 18 h8 v6 l-4 3 l-4 -3z"/><path d="M86 18 h8 v6 l-4 3 l-4 -3z"/><path d="M132 18 h8 v6 l-4 3 l-4 -3z"/>
    <path d="M40 56 h8 v6 l-4 3 l-4 -3z"/><path d="M86 56 h8 v6 l-4 3 l-4 -3z"/><path d="M132 56 h8 v6 l-4 3 l-4 -3z"/></g></svg>
  <div class="h" style="left:26px;top:30px;width:36px;text-align:center">LOREM IPSUM</div>
  <div class="h" style="left:72px;top:30px;width:36px;text-align:center">LOREM IPSUM</div>
  <div class="h" style="left:118px;top:30px;width:36px;text-align:center">LOREM IPSUM</div>
  <div class="h" style="left:26px;top:68px;width:36px;text-align:center">LOREM IPSUM</div>
  <div class="h" style="left:72px;top:68px;width:36px;text-align:center">LOREM IPSUM</div>
  <div class="h" style="left:118px;top:68px;width:36px;text-align:center">LOREM IPSUM</div>
  <div class="p" style="left:29px;top:35px;width:30px;text-align:center">Lorem ipsum dolor sit amet consectetur</div>
  <div class="p" style="left:75px;top:35px;width:30px;text-align:center">Lorem ipsum dolor sit amet consectetur</div>
  <div class="p" style="left:121px;top:35px;width:30px;text-align:center">Lorem ipsum dolor sit amet consectetur</div>
  <div class="p" style="left:29px;top:73px;width:30px;text-align:center">Lorem ipsum dolor sit amet consectetur</div>
  <div class="p" style="left:75px;top:73px;width:30px;text-align:center">Lorem ipsum dolor sit amet consectetur</div>
  <div class="p" style="left:121px;top:73px;width:30px;text-align:center">Lorem ipsum dolor sit amet consectetur</div>
  <div class="footer">TARN RIDGE</div>
</section>

<section class="slide" style="left:266px;top:418px">
  <div class="slide-title">EDIT TITLE HERE</div>
  <div class="ico" style="left:20px;top:22px;width:7px;height:7px;background:#2e3440"></div>
  <div class="ico" style="left:20px;top:40px;width:7px;height:7px;background:#2e3440"></div>
  <div class="ico" style="left:20px;top:58px;width:7px;height:7px;background:#2e3440"></div>
  <div class="ico" style="left:20px;top:76px;width:7px;height:7px;background:#2e3440"></div>
  <div class="p" style="left:32px;top:22px;width:50px"><b style="color:#175595">Lorem ipsum dolor</b><br>Lorem ipsum dolor sit amet, consectetur elit.</div>
  <div class="p" style="left:32px;top:40px;width:50px"><b style="color:#175595">Lorem ipsum dolor</b><br>Lorem ipsum dolor sit amet, consectetur elit.</div>
  <div class="p" style="left:32px;top:58px;width:50px"><b style="color:#175595">Lorem ipsum dolor</b><br>Lorem ipsum dolor sit amet, consectetur elit.</div>
  <div class="p" style="left:32px;top:76px;width:50px"><b style="color:#175595">Lorem ipsum dolor</b><br>Lorem ipsum dolor sit amet, consectetur elit.</div>
  <div class="photo" style="left:88px;top:0;width:96px;height:104px" role="img" aria-label="Hands reviewing financial charts on paper"></div>
  <div class="footer" style="right:100px">TARN RIDGE</div>
</section>

<section class="slide" style="left:472px;top:418px">
  <div class="slide-title">EDIT TITLE HERE</div>
  <div class="p" style="left:6px;top:14px;width:82px">Lorem ipsum dolor sit amet, consectetur adipiscing elit, sed do eiusmod tempor incididunt ut labore et dolore magna aliqua. Ut enim ad minim veniam, quis nostrud exercitation ullamco laboris nisi ut aliquip ex ea commodo consequat. Duis aute irure dolor in reprehenderit in voluptate velit esse cillum dolore eu fugiat nulla pariatur. Excepteur sint occaecat cupidatat non proident, sunt in culpa qui officia deserunt mollit anim id est laborum. Sed ut perspiciatis unde omnis iste natus error sit voluptatem accusantium doloremque laudantium totam rem aperiam.</div>
  <div class="photo" style="left:100px;top:12px;width:72px;height:80px;background:radial-gradient(circle at 50% 40%,#5b93d0,#c9dcf0 70%,#ffffff)" role="img" aria-label="Infographic tree illustration with clusters of blue icon circles"></div>
  <div class="footer">TARN RIDGE</div>
</section>

<section class="slide" style="left:678px;top:418px">
  <div class="slide-title">EDIT TITLE HERE</div>
  <div class="abs" style="left:84px;top:22px;width:18px;height:34px;border:1.2px solid var(--blue);border-radius:2px"></div>
  <div class="abs" style="left:87px;top:26px;width:12px;height:25px;background:#e8f0fa"></div>
  <div class="h" style="left:85px;top:37px;width:16px;text-align:center;font-size:1.8px">TARN RIDGE</div>
  <div class="p" style="left:30px;top:22px;width:46px;text-align:right"><b style="color:#175595">Lorem ipsum dolor sit</b><br>Lorem ipsum dolor sit amet consectetur.</div>
  <div class="p" style="left:30px;top:36px;width:46px;text-align:right"><b style="color:#175595">Lorem ipsum dolor sit</b><br>Lorem ipsum dolor sit amet consectetur.</div>
  <div class="p" style="left:30px;top:50px;width:46px;text-align:right"><b style="color:#175595">Lorem ipsum dolor sit</b><br>Lorem ipsum dolor sit amet consectetur.</div>
  <div class="p" style="left:110px;top:22px;width:46px"><b style="color:#175595">Lorem ipsum dolor sit</b><br>Lorem ipsum dolor sit amet consectetur.</div>
  <div class="p" style="left:110px;top:36px;width:46px"><b style="color:#175595">Lorem ipsum dolor sit</b><br>Lorem ipsum dolor sit amet consectetur.</div>
  <div class="p" style="left:110px;top:50px;width:46px"><b style="color:#175595">Lorem ipsum dolor sit</b><br>Lorem ipsum dolor sit amet consectetur.</div>
  <div class="footer">TARN RIDGE</div>
</section>

<!-- Row 5 -->
<section class="slide" style="left:60px;top:541px">
  <div class="slide-title">EDIT TITLE HERE</div>
  <div class="p" style="left:16px;top:15px;width:150px">Lorem ipsum dolor sit amet, consectetur adipiscing elit, sed do eiusmod tempor incididunt ut labore et dolore magna aliqua. Ut enim ad minim veniam, quis nostrud exercitation ullamco laboris.</div>
  <div class="band" style="left:0;top:36px;width:184px;height:30px"></div>
  <div class="photo grey" style="left:8px;top:26px;width:50px;height:44px;background:linear-gradient(135deg,#e8ecf1,#8a94a2)" role="img" aria-label="Desktop computer monitor"></div>
  <div class="ico w" style="left:78px;top:42px;width:7px;height:7px"></div>
  <div class="ico w" style="left:104px;top:42px;width:7px;height:7px"></div>
  <div class="ico w" style="left:130px;top:42px;width:7px;height:7px"></div>
  <div class="ico w" style="left:156px;top:42px;width:7px;height:7px"></div>
  <div class="p w" style="left:71px;top:52px;width:21px;text-align:center">Lorem ipsum dolor sit amet</div>
  <div class="p w" style="left:97px;top:52px;width:21px;text-align:center">Lorem ipsum dolor sit amet</div>
  <div class="p w" style="left:123px;top:52px;width:21px;text-align:center">Lorem ipsum dolor sit amet</div>
  <div class="p w" style="left:149px;top:52px;width:21px;text-align:center">Lorem ipsum dolor sit amet</div>
  <div class="footer">TARN RIDGE</div>
</section>

<section class="slide" style="left:266px;top:541px">
  <div class="slide-title">EDIT TITLE HERE</div>
  <svg width="184" height="104" viewBox="0 0 184 104"><g stroke="#8a8f97" stroke-width=".3" fill="none">
    <path d="M92 23 V28 M52 28 H132 M52 28 V32 M79 28 V32 M105 28 V32 M132 28 V32"/></g></svg>
  <div class="box" style="left:80px;top:19px;width:24px;height:4px;background:#7d838c">Title Goes Here</div>
  <div class="box" style="left:40px;top:32px;width:24px;height:4px">Title Goes Here</div>
  <div class="box" style="left:67px;top:32px;width:24px;height:4px">Title Goes Here</div>
  <div class="box" style="left:93px;top:32px;width:24px;height:4px">Title Goes Here</div>
  <div class="box" style="left:120px;top:32px;width:24px;height:4px">Title Goes Here</div>
  <div class="box" style="left:67px;top:39px;width:24px;height:4px;background:#175595">Title Goes Here</div>
  <div class="box" style="left:93px;top:39px;width:24px;height:4px;background:#175595">Title Goes Here</div>
  <div class="box" style="left:67px;top:46px;width:24px;height:4px">Title Goes Here</div>
  <div class="box" style="left:93px;top:46px;width:24px;height:4px">Title Goes Here</div>
  <div class="p" style="left:14px;top:66px;width:156px">Lorem ipsum dolor sit amet, consectetur adipiscing elit, sed do eiusmod tempor incididunt ut labore et dolore magna aliqua. Ut enim ad minim veniam, quis nostrud exercitation ullamco laboris nisi ut aliquip ex ea commodo consequat. Duis aute irure dolor in reprehenderit in voluptate velit esse cillum dolore.</div>
  <div class="footer">TARN RIDGE</div>
</section>

<section class="slide" style="left:472px;top:541px">
  <div class="slide-title">EDIT TITLE HERE</div>
  <div class="abs" style="left:18px;top:22px;width:42px;height:26px;border:.4px solid var(--line)"></div>
  <div class="abs" style="left:66px;top:22px;width:42px;height:26px;border:.4px solid var(--line);background:#e8f0fa"></div>
  <div class="abs" style="left:114px;top:22px;width:42px;height:26px;border:.4px solid var(--line)"></div>
  <div class="abs" style="left:18px;top:54px;width:42px;height:26px;border:.4px solid var(--line);background:#e8f0fa"></div>
  <div class="abs" style="left:66px;top:54px;width:42px;height:26px;border:.4px solid var(--line)"></div>
  <div class="abs" style="left:114px;top:54px;width:42px;height:26px;border:.4px solid var(--line);background:#e8f0fa"></div>
  <div class="ico" style="left:35px;top:27px;width:8px;height:8px;background:#2e3440"></div>
  <div class="ico" style="left:83px;top:27px;width:8px;height:8px"></div>
  <div class="ico" style="left:131px;top:27px;width:8px;height:8px;background:#2e3440"></div>
  <div class="ico" style="left:35px;top:59px;width:8px;height:8px"></div>
  <div class="ico" style="left:83px;top:59px;width:8px;height:8px;background:#2e3440"></div>
  <div class="ico" style="left:131px;top:59px;width:8px;height:8px"></div>
  <div class="box grey" style="left:18px;top:43px;width:42px;height:5px">LOREM IPSUM DOLOR</div>
  <div class="box" style="left:66px;top:43px;width:42px;height:5px">LOREM IPSUM DOLOR</div>
  <div class="box grey" style="left:114px;top:43px;width:42px;height:5px">LOREM IPSUM DOLOR</div>
  <div class="box" style="left:18px;top:75px;width:42px;height:5px">LOREM IPSUM DOLOR</div>
  <div class="box grey" style="left:66px;top:75px;width:42px;height:5px">LOREM IPSUM DOLOR</div>
  <div class="box" style="left:114px;top:75px;width:42px;height:5px">LOREM IPSUM DOLOR</div>
  <div class="footer">TARN RIDGE</div>
</section>

<section class="slide" style="left:678px;top:541px">
  <div class="slide-title">EDIT TITLE HERE</div>
  <svg width="184" height="104" viewBox="0 0 184 104">
    <rect x="14" y="30" width="156" height="5" fill="#1f6fc0"/>
    <g fill="#eceef1"><rect x="14" y="38" width="156" height="4"/><rect x="14" y="52" width="156" height="4"/><rect x="14" y="66" width="156" height="4"/></g>
    <g stroke="#c9ccd1" stroke-width=".3"><line x1="14" y1="45" x2="170" y2="45"/><line x1="14" y1="59" x2="170" y2="59"/><line x1="14" y1="73" x2="170" y2="73"/></g>
    <g font-family="Open Sans, sans-serif" font-size="2.3" font-weight="700" fill="#fff"><text x="20" y="33.3">Lorem</text><text x="59" y="33.3">Lorem</text><text x="98" y="33.3">Lorem</text><text x="137" y="33.3">Lorem</text></g>
    <g font-family="Open Sans, sans-serif" font-size="2.2" fill="#2e3440">
      <text x="20" y="40.8">Lorem</text><text x="59" y="40.8">Lorem</text><text x="98" y="40.8">Lorem</text><text x="137" y="40.8">Lorem</text>
      <text x="20" y="48.3">Lorem</text><text x="59" y="48.3">Lorem</text><text x="98" y="48.3">Lorem</text><text x="137" y="48.3">Lorem</text>
      <text x="20" y="54.8">Lorem</text><text x="59" y="54.8">Lorem</text><text x="98" y="54.8">Lorem</text><text x="137" y="54.8">Lorem</text>
      <text x="20" y="62.3">Lorem</text><text x="59" y="62.3">Lorem</text><text x="98" y="62.3">Lorem</text><text x="137" y="62.3">Lorem</text>
      <text x="20" y="68.8">Lorem</text><text x="59" y="68.8">Lorem</text><text x="98" y="68.8">Lorem</text><text x="137" y="68.8">Lorem</text>
      <text x="20" y="76.3">Lorem</text><text x="59" y="76.3">Lorem</text><text x="98" y="76.3">Lorem</text><text x="137" y="76.3">Lorem</text>
    </g>
  </svg>
  <div class="footer">TARN RIDGE</div>
</section>

<!-- Row 6 -->
<section class="slide" style="left:60px;top:663px">
  <div class="slide-title">EDIT TITLE HERE</div>
  <div class="photo warm" style="left:0;top:20px;width:92px;height:68px" role="img" aria-label="Team working together at laptops"></div>
  <div class="band" style="left:92px;top:20px;width:92px;height:68px"></div>
  <div class="ico w" style="left:102px;top:26px;width:7px;height:7px"></div>
  <div class="ico w" style="left:102px;top:46px;width:7px;height:7px"></div>
  <div class="ico w" style="left:102px;top:66px;width:7px;height:7px"></div>
  <div class="p w" style="left:113px;top:25px;width:62px"><b>LOREM IPSUM</b><br>Lorem ipsum dolor sit amet, consectetur adipiscing elit sed do.</div>
  <div class="p w" style="left:113px;top:45px;width:62px"><b>LOREM IPSUM</b><br>Lorem ipsum dolor sit amet, consectetur adipiscing elit sed do.</div>
  <div class="p w" style="left:113px;top:65px;width:62px"><b>LOREM IPSUM</b><br>Lorem ipsum dolor sit amet, consectetur adipiscing elit sed do.</div>
  <div class="footer">TARN RIDGE</div>
</section>

<section class="slide" style="left:266px;top:663px">
  <div class="slide-title">EDIT TITLE HERE</div>
  <div class="p" style="left:10px;top:14px;width:76px">Lorem ipsum dolor sit amet, consectetur adipiscing elit, sed do eiusmod tempor incididunt ut labore et dolore magna aliqua. Ut enim ad minim veniam, quis nostrud exercitation ullamco laboris nisi ut aliquip ex ea commodo consequat. Duis aute irure dolor in reprehenderit in voluptate velit esse cillum dolore eu fugiat nulla pariatur. Excepteur sint occaecat cupidatat non proident, sunt in culpa qui officia deserunt mollit anim id est laborum.</div>
  <svg width="184" height="104" viewBox="0 0 184 104">
    <g fill="#7d838c"><rect x="90" y="28" width="18" height="18"/><rect x="128" y="46" width="18" height="18"/><rect x="146" y="14" width="18" height="18"/></g>
    <g fill="#1f6fc0"><rect x="108" y="28" width="18" height="18"/><rect x="90" y="46" width="18" height="18" fill="#175595"/><rect x="108" y="46" width="18" height="18"/><rect x="108" y="64" width="18" height="18" fill="#175595"/><rect x="128" y="28" width="18" height="18" fill="#175595"/></g>
    <g fill="#1f6fc0"><circle cx="92" cy="92" r="1.2"/><circle cx="110" cy="92" r="1.2"/><circle cx="128" cy="92" r="1.2" fill="#7d838c"/><circle cx="146" cy="92" r="1.2"/></g>
  </svg>
  <div class="footer">TARN RIDGE</div>
</section>

<section class="slide" style="left:472px;top:663px">
  <div class="slide-title">EDIT TITLE HERE</div>
  <svg width="184" height="104" viewBox="0 0 184 104">
    <g stroke="#e1e4e8" stroke-width=".3"><line x1="10" y1="30" x2="124" y2="30"/><line x1="10" y1="45" x2="124" y2="45"/><line x1="10" y1="60" x2="124" y2="60"/><line x1="10" y1="75" x2="124" y2="75"/></g>
    <path d="M10 80 L30 60 L50 52 L70 58 L90 42 L110 50 L124 46 V80z" fill="#8fb4dc"/>
    <path d="M10 80 L30 70 L50 62 L70 66 L90 56 L110 60 L124 62 V80z" fill="#1f6fc0"/>
    <path d="M10 80 L30 76 L50 70 L70 74 L90 68 L110 72 L124 70 V80z" fill="#123f70"/>
    <g fill="#1f6fc0"><circle cx="16" cy="88" r="1"/><circle cx="32" cy="88" r="1"/><circle cx="48" cy="88" r="1" fill="#123f70"/><circle cx="64" cy="88" r="1" fill="#8fb4dc"/><circle cx="80" cy="88" r="1"/></g>
  </svg>
  <div class="abs" style="left:132px;top:14px;width:46px;height:76px;background:var(--panel)"></div>
  <div class="p" style="left:135px;top:17px;width:40px">Lorem ipsum dolor sit amet, consectetur adipiscing elit, sed do eiusmod tempor incididunt ut labore et dolore magna aliqua. Ut enim ad minim veniam, quis nostrud exercitation ullamco laboris nisi ut aliquip ex ea commodo consequat duis aute.</div>
  <div class="footer">TARN RIDGE</div>
</section>

<section class="slide" style="left:678px;top:663px">
  <div class="slide-title blue">EDIT TITLE HERE</div>
  <div class="ico" style="left:20px;top:27px;width:18px;height:18px"></div>
  <div class="ico" style="left:60px;top:27px;width:18px;height:18px"></div>
  <div class="ico" style="left:100px;top:27px;width:18px;height:18px"></div>
  <div class="ico" style="left:140px;top:27px;width:18px;height:18px"></div>
  <div class="p" style="left:15px;top:50px;width:28px;text-align:center"><b style="color:#175595">Lorem ipsum dolor</b><br>Lorem ipsum dolor sit amet, consectetur.</div>
  <div class="p" style="left:55px;top:50px;width:28px;text-align:center"><b style="color:#175595">Lorem ipsum dolor</b><br>Lorem ipsum dolor sit amet, consectetur.</div>
  <div class="p" style="left:95px;top:50px;width:28px;text-align:center"><b style="color:#175595">Lorem ipsum dolor</b><br>Lorem ipsum dolor sit amet, consectetur.</div>
  <div class="p" style="left:135px;top:50px;width:28px;text-align:center"><b style="color:#175595">Lorem ipsum dolor</b><br>Lorem ipsum dolor sit amet, consectetur.</div>
  <div class="footer">TARN RIDGE</div>
</section>

<!-- Row 7 -->
<section class="slide" style="left:60px;top:786px">
  <div class="slide-title blue">EDIT TITLE HERE</div>
  <div class="photo dark" style="left:8px;top:17px;width:68px;height:72px" role="img" aria-label="Technology network imagery in dark blue"></div>
  <svg width="184" height="104" viewBox="0 0 184 104"><g fill="#1f6fc0">
    <rect x="92" y="30" width="6" height="6" rx="1"/><rect x="122" y="30" width="6" height="6" rx="1"/><rect x="152" y="30" width="6" height="6" rx="1"/>
    <rect x="92" y="62" width="6" height="6" rx="3"/><rect x="122" y="62" width="6" height="6" rx="1"/><rect x="152" y="62" width="6" height="6" rx="3"/></g></svg>
  <div class="p" style="left:85px;top:39px;width:20px;text-align:center">Lorem ipsum dolor sit</div>
  <div class="p" style="left:115px;top:39px;width:20px;text-align:center">Lorem ipsum dolor sit</div>
  <div class="p" style="left:145px;top:39px;width:20px;text-align:center">Lorem ipsum dolor sit</div>
  <div class="p" style="left:85px;top:71px;width:20px;text-align:center">Lorem ipsum dolor sit</div>
  <div class="p" style="left:115px;top:71px;width:20px;text-align:center">Lorem ipsum dolor sit</div>
  <div class="p" style="left:145px;top:71px;width:20px;text-align:center">Lorem ipsum dolor sit</div>
  <div class="footer">TARN RIDGE</div>
</section>

<section class="slide" style="left:266px;top:786px">
  <div class="slide-title blue">EDIT TITLE HERE</div>
  <div class="p" style="left:12px;top:11px;width:160px">Lorem ipsum dolor sit amet, consectetur adipiscing elit. Aenean et tempor lorem. Suspendisse.</div>
  <div class="photo warm" style="left:12px;top:22px;width:160px;height:30px" role="img" aria-label="Four smiling team members"></div>
  <div class="box" style="left:12px;top:54px;width:39px;height:5px">A</div>
  <div class="box" style="left:52px;top:54px;width:39px;height:5px">B</div>
  <div class="box" style="left:92px;top:54px;width:39px;height:5px">C</div>
  <div class="box" style="left:132px;top:54px;width:40px;height:5px">D</div>
  <div class="p" style="left:14px;top:61px;width:35px;text-align:center">Lorem ipsum dolor sit amet, consectetur adipiscing elit.</div>
  <div class="p" style="left:54px;top:61px;width:35px;text-align:center">Lorem ipsum dolor sit amet, consectetur adipiscing elit.</div>
  <div class="p" style="left:94px;top:61px;width:35px;text-align:center">Lorem ipsum dolor sit amet, consectetur adipiscing elit.</div>
  <div class="p" style="left:134px;top:61px;width:35px;text-align:center">Lorem ipsum dolor sit amet, consectetur adipiscing elit.</div>
  <div class="footer">TARN RIDGE</div>
</section>

<section class="slide" style="left:472px;top:786px">
  <div class="slide-title blue">EDIT TITLE HERE</div>
  <div class="photo" style="left:0;top:14px;width:184px;height:90px;background:linear-gradient(110deg,#5a8fc9,#1f5fa8 50%,#7da7d6)" role="img" aria-label="Abstract financial data background"></div>
  <div class="abs" style="left:16px;top:22px;width:34px;height:24px;background:#fff"></div>
  <div class="abs" style="left:54px;top:22px;width:34px;height:24px;background:#fff"></div>
  <div class="abs" style="left:92px;top:22px;width:34px;height:24px;background:#fff"></div>
  <div class="abs" style="left:130px;top:22px;width:34px;height:24px;background:#fff"></div>
  <div class="abs" style="left:16px;top:50px;width:34px;height:24px;background:#fff"></div>
  <div class="abs" style="left:54px;top:50px;width:34px;height:24px;background:#fff"></div>
  <div class="abs" style="left:92px;top:50px;width:34px;height:24px;background:#fff"></div>
  <div class="abs" style="left:130px;top:50px;width:34px;height:24px;background:#fff"></div>
  <svg width="184" height="104" viewBox="0 0 184 104"><g fill="#1f6fc0">
    <rect x="30" y="26" width="6" height="6" rx="1"/><rect x="68" y="26" width="6" height="6" rx="1"/><rect x="106" y="26" width="6" height="6" rx="3"/><rect x="144" y="26" width="6" height="6" rx="1"/>
    <rect x="30" y="54" width="6" height="6" rx="3"/><rect x="68" y="54" width="6" height="6" rx="1"/><rect x="106" y="54" width="6" height="6" rx="3"/><rect x="144" y="54" width="6" height="6" rx="3"/></g></svg>
  <div class="p" style="left:16px;top:38px;width:34px;text-align:center">Lorem ipsum</div>
  <div class="p" style="left:54px;top:38px;width:34px;text-align:center">Lorem ipsum</div>
  <div class="p" style="left:92px;top:38px;width:34px;text-align:center">Lorem ipsum</div>
  <div class="p" style="left:130px;top:38px;width:34px;text-align:center">Lorem ipsum</div>
  <div class="p" style="left:16px;top:66px;width:34px;text-align:center">Lorem ipsum</div>
  <div class="p" style="left:54px;top:66px;width:34px;text-align:center">Lorem ipsum</div>
  <div class="p" style="left:92px;top:66px;width:34px;text-align:center">Lorem ipsum</div>
  <div class="p" style="left:130px;top:66px;width:34px;text-align:center">Lorem ipsum</div>
</section>

<section class="slide" style="left:678px;top:786px">
  <div class="slide-title">EDIT TITLE HERE</div>
  <svg width="184" height="104" viewBox="0 0 184 104">
    <path d="M14 76 H170" stroke="#8a8f97" stroke-width=".4"/>
    <g stroke="#1f6fc0" stroke-width=".4" fill="#fff">
      <circle cx="24" cy="52" r="8"/><circle cx="48" cy="44" r="8"/><circle cx="72" cy="52" r="8"/><circle cx="96" cy="44" r="8"/><circle cx="120" cy="52" r="8"/><circle cx="144" cy="44" r="8"/><circle cx="166" cy="52" r="7"/></g>
    <g stroke="#8a8f97" stroke-width=".3" stroke-dasharray="1 1"><line x1="24" y1="62" x2="24" y2="76"/><line x1="48" y1="54" x2="48" y2="76"/><line x1="72" y1="62" x2="72" y2="76"/><line x1="96" y1="54" x2="96" y2="76"/><line x1="120" y1="62" x2="120" y2="76"/><line x1="144" y1="54" x2="144" y2="76"/><line x1="166" y1="61" x2="166" y2="76"/></g>
    <g fill="#1f6fc0"><circle cx="24" cy="66" r="2.2"/><circle cx="48" cy="58" r="2.2"/><circle cx="72" cy="66" r="2.2"/><circle cx="96" cy="58" r="2.2"/><circle cx="120" cy="66" r="2.2"/><circle cx="144" cy="58" r="2.2"/><circle cx="166" cy="66" r="2.2"/></g>
    <g font-family="Open Sans, sans-serif" font-size="2.1" font-weight="700" fill="#2e3440" text-anchor="middle">
      <text x="24" y="52.7">Lorem</text><text x="48" y="44.7">Lorem</text><text x="72" y="52.7">Lorem</text><text x="96" y="44.7">Lorem</text><text x="120" y="52.7">Lorem</text><text x="144" y="44.7">Lorem</text><text x="166" y="52.7">Lorem</text></g>
  </svg>
  <div class="footer">TARN RIDGE</div>
</section>

<!-- Row 8 -->
<section class="slide" style="left:60px;top:908px">
  <div class="slide-title">EDIT TITLE HERE</div>
  <div class="p" style="left:6px;top:16px;width:48px">Lorem ipsum dolor sit amet, consectetur adipiscing elit, sed do eiusmod tempor incididunt ut labore et dolore magna aliqua. Ut enim ad minim veniam, quis nostrud exercitation ullamco laboris nisi ut aliquip ex ea commodo consequat duis aute irure dolor in reprehenderit.</div>
  <div class="band" style="left:58px;top:16px;width:86px;height:70px"></div>
  <div class="photo grey" style="left:144px;top:16px;width:40px;height:70px" role="img" aria-label="Keyboard and documents close-up"></div>
  <div class="h w" style="left:62px;top:20px;width:36px;text-align:center">Lorem ipsum</div>
  <div class="h w" style="left:102px;top:20px;width:38px;text-align:center">Lorem ipsum</div>
  <div class="p w" style="left:62px;top:25px;width:36px">Lorem ipsum dolor sit amet, consectetur adipiscing elit sed do eiusmod tempor incididunt ut labore et dolore magna aliqua enim.</div>
  <div class="p w" style="left:102px;top:25px;width:38px">Lorem ipsum dolor sit amet, consectetur adipiscing elit sed do eiusmod tempor incididunt ut labore et dolore magna aliqua enim.</div>
  <div class="footer">TARN RIDGE</div>
</section>

<section class="slide" style="left:266px;top:908px">
  <div class="slide-title blue">EDIT TITLE HERE</div>
  <div class="photo grey" style="left:8px;top:22px;width:62px;height:60px" role="img" aria-label="Hand on a keyboard with coins"></div>
  <div class="p" style="left:78px;top:22px;width:94px">Lorem ipsum dolor sit amet, consectetur adipiscing elit, sed do eiusmod tempor incididunt ut labore et dolore magna aliqua. Ut enim ad minim veniam, quis nostrud exercitation ullamco laboris nisi ut aliquip ex ea commodo consequat. Duis aute irure dolor in reprehenderit.</div>
  <div class="ico" style="left:92px;top:64px;width:6px;height:6px;border-radius:1px"></div>
  <div class="ico" style="left:120px;top:64px;width:6px;height:6px;border-radius:1px"></div>
  <div class="ico" style="left:148px;top:64px;width:6px;height:6px;border-radius:1px"></div>
  <div class="p" style="left:83px;top:73px;width:24px;text-align:center">Lorem ipsum</div>
  <div class="p" style="left:111px;top:73px;width:24px;text-align:center">Lorem ipsum</div>
  <div class="p" style="left:139px;top:73px;width:24px;text-align:center">Lorem ipsum</div>
  <div class="footer">TARN RIDGE</div>
</section>

<section class="slide" style="left:472px;top:908px">
  <div class="slide-title blue">EDIT TITLE HERE</div>
  <div class="band" style="left:0;top:20px;width:84px;height:70px"></div>
  <div class="h w" style="left:22px;top:32px;font-size:3.6px">LOREM IPSUM</div>
  <div class="p w" style="left:22px;top:38px;width:56px">Lorem ipsum dolor sit amet, consectetur adipiscing elit, sed do eiusmod tempor incididunt ut labore et dolore magna aliqua. Ut enim ad minim veniam, quis nostrud exercitation ullamco laboris nisi ut aliquip ex ea commodo consequat.</div>
  <div class="photo grey" style="left:84px;top:20px;width:92px;height:70px" role="img" aria-label="Team meeting in a glass-walled boardroom"></div>
  <div class="footer">TARN RIDGE</div>
</section>

<section class="slide" style="left:678px;top:908px">
  <div class="slide-title blue">EDIT TITLE HERE</div>
  <div class="photo grey" style="left:40px;top:18px;width:110px;height:70px;background:linear-gradient(135deg,#eef0f3,#d5d9df);border-radius:30%" role="img" aria-label="World map in light grey"></div>
  <div class="ico" style="left:40px;top:22px;width:6px;height:6px;background:#2e3440"></div>
  <div class="ico" style="left:72px;top:44px;width:6px;height:6px;background:#2e3440"></div>
  <div class="ico" style="left:34px;top:58px;width:6px;height:6px;background:#2e3440"></div>
  <div class="ico" style="left:122px;top:30px;width:6px;height:6px;background:#2e3440"></div>
  <div class="ico" style="left:124px;top:62px;width:6px;height:6px;background:#2e3440"></div>
  <div class="p" style="left:8px;top:22px;width:26px"><b style="color:#175595">Lorem ipsum</b><br>Lorem ipsum dolor sit amet elit.</div>
  <div class="p" style="left:8px;top:66px;width:24px"><b style="color:#175595">Lorem ipsum</b><br>Lorem ipsum dolor sit amet elit.</div>
  <div class="p" style="left:70px;top:52px;width:26px"><b style="color:#175595">Lorem ipsum</b><br>Lorem ipsum dolor sit amet elit.</div>
  <div class="p" style="left:146px;top:26px;width:28px"><b style="color:#175595">Lorem ipsum</b><br>Lorem ipsum dolor sit amet elit.</div>
  <div class="p" style="left:146px;top:60px;width:28px"><b style="color:#175595">Lorem ipsum</b><br>Lorem ipsum dolor sit amet elit.</div>
  <div class="footer">TARN RIDGE</div>
</section>

<!-- Row 9 -->
<section class="slide" style="left:60px;top:1032px">
  <div class="slide-title blue">EDIT TITLE HERE</div>
  <div class="abs" style="left:10px;top:16px;width:124px;height:72px;background:var(--panel)"></div>
  <div class="box" style="left:14px;top:20px;width:4px;height:4px">1</div>
  <div class="box" style="left:14px;top:30px;width:4px;height:4px">2</div>
  <div class="box" style="left:14px;top:40px;width:4px;height:4px">3</div>
  <div class="box" style="left:14px;top:50px;width:4px;height:4px">4</div>
  <div class="box" style="left:14px;top:60px;width:4px;height:4px">5</div>
  <div class="box" style="left:14px;top:70px;width:4px;height:4px">6</div>
  <div class="abs" style="left:22px;top:17px;width:88px;font-size:2.2px;line-height:10px;color:var(--ink)">Lorem ipsum dolor sit amet, consectetur adipiscing elit<br>Lorem ipsum dolor sit amet, consectetur adipiscing elit<br>Lorem ipsum dolor sit amet, consectetur adipiscing elit<br>Lorem ipsum dolor sit amet, consectetur adipiscing elit<br>Lorem ipsum dolor sit amet, consectetur adipiscing elit<br>Lorem ipsum dolor sit amet, consectetur adipiscing elit</div>
  <div class="photo" style="left:112px;top:18px;width:60px;height:58px" role="img" aria-label="Modern office building exterior"></div>
  <div class="footer">TARN RIDGE</div>
</section>

<section class="slide" style="left:266px;top:1032px">
  <div class="slide-title">EDIT TITLE HERE</div>
  <div class="photo grey" style="left:10px;top:26px;width:26px;height:26px" role="img" aria-label="Business portrait"></div>
  <div class="photo warm" style="left:37px;top:26px;width:26px;height:26px" role="img" aria-label="Coffee and notebook"></div>
  <div class="photo grey" style="left:64px;top:26px;width:26px;height:26px" role="img" aria-label="Business portrait"></div>
  <div class="photo" style="left:91px;top:26px;width:26px;height:26px" role="img" aria-label="Office workspace"></div>
  <div class="photo grey" style="left:118px;top:26px;width:26px;height:26px" role="img" aria-label="Business portrait"></div>
  <div class="photo dark" style="left:145px;top:26px;width:27px;height:26px" role="img" aria-label="City buildings"></div>
  <div class="band" style="left:10px;top:52px;width:26px;height:30px"></div>
  <div class="band" style="left:37px;top:52px;width:26px;height:30px;background:#7d838c"></div>
  <div class="band" style="left:64px;top:52px;width:26px;height:30px"></div>
  <div class="band" style="left:91px;top:52px;width:26px;height:30px;background:#7d838c"></div>
  <div class="band" style="left:118px;top:52px;width:26px;height:30px"></div>
  <div class="band" style="left:145px;top:52px;width:27px;height:30px;background:#7d838c"></div>
  <div class="p w" style="left:10px;top:53px;width:26px;text-align:center;font-weight:700">TITLE HERE</div>
  <div class="p w" style="left:37px;top:53px;width:26px;text-align:center;font-weight:700">TITLE HERE</div>
  <div class="p w" style="left:64px;top:53px;width:26px;text-align:center;font-weight:700">TITLE HERE</div>
  <div class="p w" style="left:91px;top:53px;width:26px;text-align:center;font-weight:700">TITLE HERE</div>
  <div class="p w" style="left:118px;top:53px;width:26px;text-align:center;font-weight:700">TITLE HERE</div>
  <div class="p w" style="left:145px;top:53px;width:27px;text-align:center;font-weight:700">TITLE HERE</div>
  <div class="p w" style="left:12px;top:57px;width:22px">Lorem ipsum dolor sit amet elit sed.</div>
  <div class="p w" style="left:39px;top:57px;width:22px">Lorem ipsum dolor sit amet elit sed.</div>
  <div class="p w" style="left:66px;top:57px;width:22px">Lorem ipsum dolor sit amet elit sed.</div>
  <div class="p w" style="left:93px;top:57px;width:22px">Lorem ipsum dolor sit amet elit sed.</div>
  <div class="p w" style="left:120px;top:57px;width:22px">Lorem ipsum dolor sit amet elit sed.</div>
  <div class="p w" style="left:147px;top:57px;width:22px">Lorem ipsum dolor sit amet elit sed.</div>
  <div class="footer">TARN RIDGE</div>
</section>

<section class="slide" style="left:472px;top:1032px">
  <div class="band" style="left:0;top:0;width:184px;height:52px"></div>
  <div class="abs" style="left:8px;top:5px;font-size:8px;font-weight:800;color:#fff;line-height:1">“</div>
  <div class="abs" style="left:20px;top:13px;width:144px;text-align:center;font-size:3px;font-weight:700;color:#fff;line-height:1.3">“Lorem ipsum dolor sit amet, consectetur adipiscing elit. Phasellus sodales, ligula ultrices tempus tristique, tellus justo aliquam dui, nec lorem ipsum dolor sit amet, consectetur adipiscing elit, lorem ipsum dolor sit amet, consectetur adipiscing.”</div>
  <div class="abs" style="right:8px;top:38px;font-size:8px;font-weight:800;color:#fff;line-height:1">”</div>
  <div class="photo grey" style="left:80px;top:44px;width:24px;height:24px;border-radius:50%;border:1px solid #fff" role="img" aria-label="Portrait of the quoted speaker"></div>
  <div class="abs" style="left:62px;top:71px;width:60px;text-align:center;font-size:3px;font-weight:700;color:var(--ink)">Nora Lind</div>
  <div class="p" style="left:62px;top:75px;width:60px;text-align:center">Chief Operating Officer</div>
</section>

<section class="slide" style="left:678px;top:1032px">
  <div class="photo" style="left:0;top:0;width:184px;height:104px;background:linear-gradient(100deg,#5b7fa8,#28507f 45%,#c99a6b)" role="img" aria-label="Group of professionals celebrating"></div>
  <div class="abs" style="left:0;top:0;width:100px;height:104px;background:rgba(31,90,160,.55)"></div>
  <div class="abs" style="left:34px;top:48px;font-size:6px;font-weight:700;color:#fff;line-height:1">THANK YOU</div>
</section>

</main>
</body>
</html>
```